I need a book cover for my book titled Sunny Porch! The subtitle is Quiet Orchard Days and the the author is Marisol Dunleavy. I want the attached photo included on the cover, plus the words "I never met a chicken wing I didn't like!" The book size is 5.06 x 7.81 in. and is 146 pages. For the color scheme, I like a chocolate brown cover with aqua blue letters. (Please note that you don't have to use these colors. Feel free to use this color scheme or whatever you colors you like!)

• Please include my photo for the back cover, along with this text:

Sunny Porch! I was tired of being tired! I was tired of acid reflux, body stiffness, and being overweight. To make matters worse, I suffered from back pain, constipation, leg pain, and lack of sleep. If you are tired of looking to medical test for your answers, this is the book for you. The key was the day I decided to make “me” a priority by being #1 on my “to-do” list.

Our healthcare system seems to be more concerned about treating illness than they are about preventing it; which is why we have so many problems with our health and wellness. That’s why I’m going to give you insights into nutrition, health care, and the pharmaceutical industry.

I’m also going to give you some insights into exercise, supplements, detoxing and essential oils; as well as what goes into your grocery cart and the foods you feed your family.

Because you’re reading this I know you’re ready to live your best life, Sunny Porch! is for you.

Here’s to a healthy you!

Here's a brief bio about the author for the back cover:

Marisol lives in Chicago with her husband, Dr. Wendell, and has three adult children. She is probably one of the most private people you will meet – BUT HAD to tell her story!

```html
<!DOCTYPE html>
<html lang="en">
<head>
<meta charset="utf-8">
<title>Sunny Porch! – Book Cover</title>
<link rel="stylesheet" href="https://fonts.googleapis.com/css2?family=Cinzel:wght@400;700&family=Kaushan+Script&display=swap">
<style>
  :root {
    --stage-top: #f1f1f1;
    --stage-bottom: #d6d6d6;
    --cocoa-light: #8a5640;
    --cocoa-mid: #6b3a28;
    --cocoa-dark: #3d1a12;
    --band-tan: #8c5a3f;
    --band-deep: #4a2218;
    --ink-white: #ffffff;
    --ink-cream: #f3e6dc;
    --rule: #a07a66;
    --art-warm: #a9553a;
    --art-soft: #c99a82;
  }
  * { box-sizing: border-box; margin: 0; padding: 0; }
  html, body { width: 1200px; height: 848px; overflow: hidden; }
  body {
    background: linear-gradient(180deg, var(--stage-top), var(--stage-bottom));
    font-family: "Cinzel", serif;
    position: relative;
  }
  .cover {
    position: absolute;
    top: 74px;
    width: 453px;
    height: 700px;
    color: var(--ink-white);
    background: radial-gradient(ellipse at 50% 35%, var(--cocoa-light) 0%, var(--cocoa-mid) 45%, var(--cocoa-dark) 100%);
    box-shadow: 0 14px 30px rgba(0,0,0,.3);
    overflow: hidden;
  }
  .front { left: 120px; }
  .back { left: 627px; }

  .title {
    font-weight: 700;
    text-align: center;
    line-height: 1;
    text-shadow: 0 2px 4px rgba(0,0,0,.45);
    font-variant: small-caps;
  }
  .subtitle {
    text-align: center;
    font-variant: small-caps;
    color: var(--ink-cream);
    text-shadow: 0 2px 3px rgba(0,0,0,.4);
  }
  .front .title { margin-top: 98px; font-size: 62px; }
  .front .subtitle { font-size: 31px; margin-top: 4px; }

  .hero-art {
    position: absolute;
    left: 40px; top: 250px;
    width: 373px; height: 220px;
    background: linear-gradient(135deg, var(--art-soft) 0%, var(--art-warm) 100%);
  }
  .tagline {
    position: absolute;
    left: 0; right: 0; top: 498px;
    font-family: "Kaushan Script", cursive;
    font-size: 36px;
    line-height: 1.15;
    text-align: center;
    text-shadow: 0 2px 4px rgba(0,0,0,.4);
  }
  .author-band {
    position: absolute;
    left: 0; right: 0; top: 604px;
    height: 64px;
    background: var(--band-deep);
    border-top: 14px solid var(--band-tan);
    display: flex; align-items: center; justify-content: center;
  }
  .author-band .author-name {
    font-size: 24px;
    letter-spacing: 1px;
    text-transform: uppercase;
  }

  .back .title { margin-top: 52px; font-size: 46px; }
  .back .subtitle { font-size: 24px; margin-top: 2px; }
  .blurb {
    margin: 18px 28px 0 28px;
    font-size: 11px;
    line-height: 1.38;
    font-variant: small-caps;
    color: var(--ink-cream);
  }
  .blurb p + p { margin-top: 11px; }
  .divider-dots {
    display: flex; gap: 5px; justify-content: center;
    margin-top: 12px; padding-left: 30px;
  }
  .divider-dots span { width: 8px; height: 8px; border-radius: 50%; background: var(--ink-white); }
  .bio {
    position: absolute;
    left: 28px; top: 490px; width: 260px;
    font-size: 13.5px;
    line-height: 1.3;
    font-variant: small-caps;
  }
  .bio p + p { margin-top: 10px; }
  .author-photo {
    position: absolute;
    right: 14px; top: 470px;
    width: 148px; height: 200px;
    border: 3px solid #5a1e16;
    background: linear-gradient(160deg, #6b5a4c 0%, #a77a55 45%, #3b2a20 100%);
  }
  .credit {
    position: absolute;
    left: 28px; top: 630px;
  }
  .credit .label {
    font-size: 12px; text-transform: uppercase;
    border-bottom: 1px solid var(--rule);
    width: 180px; padding-bottom: 2px;
  }
  .credit .author-name { font-size: 17px; text-transform: uppercase; margin-top: 4px; }
</style>
</head>
<body>

<section class="cover front">
  <h1 class="title">Sunny Porch!</h1>
  <h2 class="subtitle">Quiet Orchard Days</h2>
  <div class="hero-art" role="img" aria-label="Photo of a plate of glazed chicken wings with vegetables and dip"></div>
  <p class="tagline">"I never met a chicken wing<br>I didn't like!"</p>
  <div class="author-band"><span class="author-name">Marisol Dunleavy</span></div>
</section>

<section class="cover back">
  <h1 class="title">Sunny Porch!</h1>
  <h2 class="subtitle">Quiet Orchard Days</h2>
  <div class="blurb">
    <p>Sunny Porch! I was tired of being tired! I was tired of acid reflux, body stiffness, and being overweight. To make matters worse, I suffered from back pain, constipation, leg pain, and lack of sleep. If you are tired of looking to medical test for your answers, this is the book for you. The key was the day I decided to make "me" a priority by being #1 on my "to-do" list.</p>
    <p>Our healthcare system seems to be more concerned about treating illness than they are about preventing it; which is why we have so many problems with our health and wellness. That's why I'm going to give you insights into nutrition, health care, and the pharmaceutical industry.</p>
    <p>I'm also going to give you some insights into exercise, supplements, detoxing and essential oils; as well as what goes into your grocery cart and the foods you feed your family.</p>
    <p>Because you're reading this I know you're ready to live your best life, Sunny Porch! is for you.</p>
  </div>
  <div class="divider-dots"><span></span><span></span><span></span></div>
  <div class="bio">
    <p>Marisol lives in Chicago with her husband, Dr. Wendell, and has three adult children.</p>
    <p>She is probably one of the most private people you will meet – but had to tell her story!</p>
  </div>
  <div class="author-photo" role="img" aria-label="Portrait photo of the author"></div>
  <div class="credit">
    <div class="label">Author</div>
    <div class="author-name">Marisol Dunleavy</div>
  </div>
</section>

</body>
</html>
```